Flyer Design Project - Nail Art

This is a flyer project for a nail saloon/cosmetics/beauty outlet. The flyer will be double-sided displaying information and/or pictures on both sides.

We would like to have the flyer in C6 format.

Prefered Background of the flyer will be black. Several image will be attached to this description (or may have been already) to help you see what we'd like to see.

FRONT SIDE: On this side we need some Text displayed; informative yet also clearly indicating that it will work as a voucher. Stylish yet professional.

BACK SIDE: Some pictures displayed to allow people to take a look at some of our work. How those pictures are displayed is entirely up to the designer. One idea that we had would be to have four pictures with the logo in the middle - however, this is entirely up to you guys.
Updates

Received a lot of great designs already, thanks!

Will provide feedback starting tomorrow; for now we'll just have a look. Thanks for your patience.

Project Deadline Extended
Reason: Only 10 days seemed a bit tight. :) We'll extend the deadline by 5 days.

Hey guys,

something important came up so I can't comment or submit feedback for two days.

Will get back to you all asap.

Cheers!

Project Deadline Extended
Reason: Extending the deadline for just a few days! Please do not submit any more designs. Thanks you!

Industry/Entity Type

Cosmetics

Requirements
Must have
• + Text below MUST be included on the front page.
+ C6 Format
+ Pictures displayed on the back
+ Logo Included

TEXT ON THE FRONT SIDE:

KL Glanzwerk - für außergewöhnliche Eyecatcher!
Mobiler Service

GUTSCHEIN

NEUANLAGE: 55.- Euro / 65.- CHF (statt 65.- Euro / 80.- CHF)
inklusive French und Verziehrung/Nailart auf 2 Nägel

AUFÜLLEN: 40,- Euro / 50.- CHF (statt 45.- Euro / 55.- CHF)

TERMINE UNTER 0664-3817056

Dieser Flyer dient als Gutschein. Am vereinbarten Termin
vorlegen!

Facebook: KL Glanzwerk
Mail: kl.glanzwerk@postfeld.example
Web: www.kl-glanzwerk.example

-
By designer Request - Rough english Translation of the Flyer text
-

Mobiler Service

[Voucher]
GUTSCHEIN

[Here the prices for completely new sets are listed]
[including French and Nailart on 2 nails]

[here the prices for renewing an existing set are listed]

[Contact telephone number]

[This flyer serves as a voucher. Bring it with you when you have an appointment]
vorlegen!

[Contact Details]
Facebook: KL Glanzwerk
Web: www.kl-glanzwerk.example
Nice to have
• FONT: Beautiful ES

NAILS labeled RED on the front page

PREFERED COLORS: Black/Red

```html
<!DOCTYPE html>
<html lang="de">
<head>
<meta charset="utf-8">
<title>KL Glanzwerk – Gutschein Flyer</title>
<link rel="stylesheet" href="https://fonts.googleapis.com/css2?family=Pinyon+Script&display=swap">
<style>
  :root {
    --page: #ffffff;
    --ink: #ffffff;
    --black: #140709;
    --black-deep: #0a0304;
    --red: #8e1a1e;
    --red-light: #a5262a;
    --red-line: #5a1416;
    --photo-warm: #c99a86;
  }
  * { box-sizing: border-box; margin: 0; padding: 0; }
  html, body {
    width: 933px; height: 1200px; overflow: hidden;
    background: var(--page);
  }
  body { position: relative; font-family: "Pinyon Script", cursive; color: var(--ink); }

  .flyer-side {
    position: absolute; left: 57px; width: 778px;
    background: linear-gradient(160deg, var(--black) 0%, var(--black-deep) 100%);
    overflow: hidden;
  }
  .front { top: 0; height: 562px; }
  .back { top: 595px; height: 575px; }

  .red-band {
    position: absolute; top: 0; bottom: 0;
    background: radial-gradient(ellipse at 50% 40%, var(--red-light) 0%, var(--red) 75%);
  }
  .front .red-band { left: 478px; width: 244px; }
  .back .red-band { left: 11px; width: 167px; }
  .band-cap {
    position: absolute; left: 11px; width: 167px; top: 0; height: 50px;
    background: var(--red-light); border-bottom: 1px solid var(--red-line);
  }
  .back-rule {
    position: absolute; left: 178px; right: 0; top: 50px; height: 1px;
    background: var(--red-line);
  }

  .brand-mark {
    position: absolute; display: flex; align-items: center; justify-content: center; gap: 8px;
    color: var(--ink); white-space: nowrap;
  }
  .brand-mark .square { width: 11px; height: 11px; background: var(--ink); flex: none; }
  .front .brand-mark { left: 478px; width: 244px; top: 165px; font-size: 26px; }
  .back .brand-mark { left: 11px; width: 167px; top: 140px; font-size: 22px; }

  .photo { position: absolute; }
  .photo-small { width: 98px; height: 76px; left: 408px;
    background: linear-gradient(135deg, #2a1517, var(--photo-warm) 60%, #3a1a1c); }

  .front-text { position: absolute; left: 22px; top: 24px; width: 400px; }
  .title { font-size: 30px; line-height: 40px; }
  .title-rule { width: 200px; height: 2px; background: var(--ink); margin: 2px 0 10px; }
  .tagline { font-size: 23px; line-height: 30px; }
  .service { font-size: 14px; line-height: 22px; opacity: .85; margin-left: 10px; }
  .prices { margin-top: 24px; font-size: 15px; line-height: 31px; font-weight: 700; }

  .voucher-note { position: absolute; left: 15px; top: 395px; width: 460px;
    font-size: 14px; line-height: 20px; font-weight: 700; text-align: center; }
  .contact { position: absolute; left: 10px; top: 438px; width: 466px; text-align: center; font-weight: 700; }
  .contact .phone { font-size: 20px; line-height: 36px; letter-spacing: 1px; }
  .contact .line { font-size: 15px; line-height: 36px; white-space: nowrap; }

  .band-heading { position: absolute; width: 244px; left: 478px; text-align: center; }
  .band-name { top: 296px; font-size: 30px; }
  .band-voucher { top: 338px; font-size: 27px; letter-spacing: 3px; }

  .gallery-photo { width: 242px; height: 120px; }
  .tone-green { background: linear-gradient(135deg, #c8c060, #8fbf3a 50%, #d9a88a); }
  .tone-violet { background: linear-gradient(135deg, #e8e4dc, #c99b88 50%, #6c3f7a); }
  .tone-orange { background: linear-gradient(135deg, #e6e2dc, #c58460 50%, #d46a1c); }
  .tone-black { background: linear-gradient(135deg, #dcdad8, #b58a7c 50%, #1a1214); }
  .tone-emerald { background: linear-gradient(135deg, #3a3340, #c9a090 50%, #1f6a3a); }
  .tone-pink { background: linear-gradient(135deg, #e8e6e2, #d8a595 50%, #c8637e); }

  .back-name { position: absolute; left: 11px; width: 167px; top: 238px; text-align: center; font-size: 26px; }
</style>
</head>
<body>

<section class="flyer-side front" aria-label="Vorderseite Gutschein">
  <div class="red-band"></div>

  <div class="photo photo-small" style="top:30px" role="img" aria-label="Foto: Hand mit roten Nägeln"></div>
  <div class="photo photo-small" style="top:123px" role="img" aria-label="Foto: Hand mit rot verzierten Nägeln"></div>

  <div class="front-text">
    <div class="title">KL Glanzwerk</div>
    <div class="title-rule"></div>
    <div class="tagline">für außergewöhnliche Eyecatcher!</div>
    <div class="service">Mobiler Service</div>
    <div class="prices">
      NEUANLAGE: 55.- Euro / 65.- CHF (statt 65.-<br>
      Euro / 80.- CHF) inklusive French und Verziehrung/<br>
      Nailart auf 2 Nägel<br>
      AUFÜLLEN: 40,- Euro / 50.- CHF (statt 45.-<br>
      Euro / 55.- CHF) inklusive French und Verziehrung/<br>
      Nailart auf 2 Nägel
    </div>
  </div>

  <p class="voucher-note">Dieser Flyer dient als Gutschein. Am vereinbarten Termin vorlegen!</p>

  <div class="contact">
    <div class="phone">TERMINE UNTER 0664-3817056</div>
    <div class="line">Facebook: KL Glanzwerk Mail: kl.glanzwerk@postfeld.example</div>
    <div class="line">Web: www.kl-glanzwerk.example</div>
  </div>

  <div class="brand-mark"><span class="square"></span>KL Glanzwerk</div>
  <div class="band-heading band-name">KL Glanzwerk</div>
  <div class="band-heading band-voucher">GUTSCHEIN</div>
</section>

<section class="flyer-side back" aria-label="Rückseite Galerie">
  <div class="red-band"></div>
  <div class="band-cap"></div>
  <div class="back-rule"></div>

  <div class="brand-mark"><span class="square"></span>KL Glanzwerk</div>
  <div class="back-name">KL Glanzwerk</div>

  <div class="photo gallery-photo tone-green" style="left:223px; top:85px" role="img" aria-label="Foto: Nägel mit grünem Design"></div>
  <div class="photo gallery-photo tone-violet" style="left:476px; top:85px" role="img" aria-label="Foto: Nägel mit violetten Spitzen"></div>
  <div class="photo gallery-photo tone-orange" style="left:223px; top:222px" role="img" aria-label="Foto: Nägel mit orangem Muster"></div>
  <div class="photo gallery-photo tone-black" style="left:476px; top:222px" role="img" aria-label="Foto: Nägel mit schwarzem French"></div>
  <div class="photo gallery-photo tone-emerald" style="left:223px; top:353px" role="img" aria-label="Foto: Nägel mit grünem und violettem Nailart"></div>
  <div class="photo gallery-photo tone-pink" style="left:476px; top:353px" role="img" aria-label="Foto: Nägel mit rosa Design"></div>
</section>

</body>
</html>
```